Harborline Power Works, LLC New Business Card Design Project

Please do not submit multiple designs that look similar. Many submittals of nearly the same design will result in auto rejection. Please do not submit a design unless you know how to provide a PDF with recognizable text that I can modify and update using Adobe Acrobat. I do not use Adobe Photoshop. Please design a business card using the attached HPW logo. Be creative. Do at least 2-3 different designs. One side should have the logo large with the URL www.HPW-KV.com. The other side of the card should have the name Marcus Pellow. License number 524038. Phone number 555-555-0143. Email service@HPW-KV.com. Physical address 742 Maple Orchard Road, Suite 3, Ashgrove, KV. 06099. The company name should also be spelled out somewhere, Harborline Power Works, LLC. Please ensure there is no tiny font. Please also ensure that there is nothing near the edges that might get cut off during printing. It will be 3.5" x 2" horizontal standard business card. I use CardQuarry.com to order. The customer has said they want the business card to use the attached look and color scheme. Please do not submit a design unless you know how to provide a PDF with recognizable text that I can modify and update using Adobe Acrobat. I do not use Adobe Photoshop.
Target Market(s)
Read all instructions above.
Industry/Entity Type
Contact Information for Business Card
Requirements
Must have
- Read all instructions above.
Nice to have
Should not have

```html
<!DOCTYPE html>
<html lang="en">
<head>
<meta charset="utf-8">
<title>Harborline Power Works, LLC – Business Card</title>
<link href="https://fonts.googleapis.com/css2?family=Poppins:wght@400;500;600;700&display=swap" rel="stylesheet">
<style>
  :root {
    --backdrop: #1c1c1d;
    --card: #0f0f10;
    --gold: #d6a92a;
    --silver: #b9b9bb;
    --white: #f2f2f2;
    --rule: #8a8a8a;
  }
  * { box-sizing: border-box; margin: 0; padding: 0; }
  html, body { width: 1200px; height: 1200px; overflow: hidden; }
  body {
    background: var(--backdrop);
    font-family: "Poppins", sans-serif;
    color: var(--white);
    position: relative;
  }
  .card {
    position: absolute;
    left: 150px;
    width: 900px;
    height: 514px;
    background: var(--card);
    border-radius: 22px;
    box-shadow: 0 16px 40px rgba(0,0,0,.55);
  }
  .card--back { top: 70px; }
  .card--front { top: 616px; }

  .brand {
    position: absolute;
    display: flex;
    align-items: center;
    gap: 18px;
    font-weight: 700;
    color: var(--silver);
    letter-spacing: 2px;
  }
  .brand__dot {
    border-radius: 50%;
    background: currentColor;
    flex: none;
  }
  .card--back .brand { left: 50%; top: 150px; transform: translateX(-50%); font-size: 120px; line-height: 1; }
  .card--back .brand__dot { width: 34px; height: 34px; }
  .back__url {
    position: absolute; left: 0; right: 0; top: 360px;
    text-align: center; font-size: 26px; font-weight: 500;
    color: var(--silver); letter-spacing: .5px;
  }

  .company {
    position: absolute; left: 70px; top: 52px;
    text-transform: uppercase; font-weight: 600; letter-spacing: 1px;
  }
  .company__line1 { color: var(--gold); font-size: 31px; line-height: 1.1; }
  .company__line2 {
    display: flex; align-items: center; gap: 12px;
    color: var(--silver); font-size: 29px; font-weight: 500; line-height: 1.1;
  }
  .company__line2::before, .company__line2::after {
    content: ""; width: 50px; height: 1.5px; background: var(--silver);
  }

  .card--front .brand {
    right: 80px; top: 160px; font-size: 96px; line-height: 1; color: var(--gold);
  }
  .card--front .brand__dot { width: 28px; height: 28px; }

  .person { position: absolute; left: 70px; top: 240px; }
  .person__name { font-size: 34px; font-weight: 600; color: var(--white); line-height: 1.15; }
  .person__license { font-size: 21px; color: var(--gold); }

  .divider {
    position: absolute; left: 60px; right: 60px; top: 330px;
    height: 1.5px; background: var(--rule);
  }
  .contacts { position: absolute; left: 70px; top: 348px; list-style: none; }
  .contacts li {
    display: flex; align-items: center; gap: 12px;
    font-size: 22px; line-height: 1.5; color: var(--white);
  }
  .contacts svg { width: 20px; height: 20px; fill: none; stroke: var(--gold); stroke-width: 1.8; }

  .address {
    position: absolute; right: 70px; top: 402px;
    text-align: right; font-size: 22px; line-height: 1.4; color: var(--white);
    font-style: normal;
  }
</style>
</head>
<body>

  <section class="card card--back" aria-label="Card back">
    <div class="brand"><span class="brand__dot"></span>HPW</div>
    <p class="back__url">www.HPW-KV.com</p>
  </section>

  <section class="card card--front" aria-label="Card front">
    <div class="company">
      <div class="company__line1">Harborline Power</div>
      <div class="company__line2">Works, LLC</div>
    </div>

    <div class="brand"><span class="brand__dot"></span>HPW</div>

    <div class="person">
      <div class="person__name">Marcus Pellow</div>
      <div class="person__license">License number 524038.</div>
    </div>

    <div class="divider"></div>

    <ul class="contacts">
      <li>
        <svg viewBox="0 0 24 24"><path d="M5 3h4l2 5-2.5 1.5a11 11 0 0 0 6 6L16 13l5 2v4a2 2 0 0 1-2 2A17 17 0 0 1 3 5a2 2 0 0 1 2-2z"/></svg>
        555-555-0143
      </li>
      <li>
        <svg viewBox="0 0 24 24"><rect x="3" y="5" width="18" height="14" rx="1"/><path d="M3 6l9 7 9-7"/></svg>
        service@HPW-KV.com
      </li>
      <li>
        <svg viewBox="0 0 24 24"><circle cx="12" cy="12" r="9"/><path d="M3 12h18M12 3c3 3 3 15 0 18M12 3c-3 3-3 15 0 18"/></svg>
        www.HPW-KV.com
      </li>
    </ul>

    <address class="address">
      742 Maple Orchard Road, Suite 3<br>
      Ashgrove, KV. 06099
    </address>
  </section>

</body>
</html>
```